Vorgan Sports Nutrition Brand needs a Packaging label

Hi all, please see the considerations for our vision.
We need a Golden Ratio packaging label design for new Sports nutrition/supplement brand. I would like to give you a little bit of background about myself and hopefully that will help you in creating the design.
I am myself into fitness. I am 33 years old at the moment and been hitting gyms consistently from 14 years old. I do use supplements of all types that helps with performance and body compositions.
Ideally I would like the brand to be able to resonate with male and female audience. The brand needs to give premium look and feel. Those people who will be associating themselves with the brand should be proud of themselves being a part of the team. That's our ideal customer persona.
In terms of colours we are open to your suggestions but do think that red should be included as a detail colour.
P.S Please check out my Instagram to learn more about ideal customer for the brand. @pelmatovv
When creating the name ''vorgan'' we wanted the name to capture two things. First a feeling that we get when we go to gyms and the feeling is excited. And secondly the name for the product or the industry and that's nutrition. We then shortened the feeling excited to Vorgan for a more catchy name.

The Nutrition information will be sent to add once we pick the design.
The pictures of brands that we admire them are attached.

Please design One label design and just resize for these products. For dimensions please refer to the Print guide attached.
Core Bulk Builder 2.25KG
Tasty Strengthmix 250G
Vigor Lift Prime 120 Tabs
Surge Rush Pre Workout 250G
Branded Shakers

Target Market(s)

Fitness / bodybuilding audience male & female mass market

Industry/Entity Type

Nutrition

Colors

Designer to choose colors to be used in the design.

Requirements
Must have
• Our logo.
• Please find it attached
Nice to have
• The transparent Logo X some where in the background almost like a watermark. In other words like a subconscious clue.
Should not have
• Organic look.

```html
<!DOCTYPE html>
<html lang="en">
<head>
<meta charset="UTF-8">
<title>Vorgan Nutrition – Lean Muscle Builder Label</title>
<link rel="stylesheet" href="https://fonts.googleapis.com/css2?family=Oswald:wght@700&family=Michroma&display=swap">
<style>
  :root {
    --page-bg: #ffffff;
    --label-black: #151515;
    --red-deep: #5e0907;
    --red-mid: #a3140f;
    --red-bright: #dc2419;
    --strip-red: #6b0d0a;
    --text-white: #ffffff;
    --text-soft: #f1d9d6;
    --silver-light: #f4f4f4;
    --silver-mid: #b9b9b9;
    --silver-dark: #7d7d7d;
    --badge-ink: #111111;
  }
  html, body {
    margin: 0;
    padding: 0;
    width: 1200px;
    height: 1000px;
    overflow: hidden;
    background: var(--page-bg);
  }
  .canvas {
    position: relative;
    width: 1200px;
    height: 1000px;
  }
  .label {
    position: absolute;
    left: 175px;
    top: 200px;
    width: 850px;
    height: 600px;
    background: var(--label-black);
    overflow: hidden;
  }
  .label-band {
    position: absolute;
    left: 0; top: 0;
    width: 850px;
    height: 376px;
    background:
      radial-gradient(ellipse 60% 90% at 60% 60%, var(--red-bright) 0%, var(--red-mid) 55%, transparent 100%),
      linear-gradient(90deg, var(--red-deep) 0%, var(--red-mid) 45%, var(--red-mid) 70%, var(--red-deep) 100%);
  }
  .brand-name {
    position: absolute;
    left: 336px;
    top: 132px;
    margin: 0;
    font-family: "Oswald", sans-serif;
    font-weight: 700;
    font-size: 104px;
    line-height: 1;
    letter-spacing: 2px;
    color: var(--text-white);
  }
  .brand-descriptor {
    position: absolute;
    left: 420px;
    top: 258px;
    margin: 0;
    font-family: "Michroma", sans-serif;
    font-size: 24px;
    letter-spacing: 7px;
    color: var(--text-white);
  }
  .product-strip {
    position: absolute;
    left: 0; top: 376px;
    width: 850px;
    height: 80px;
    background: linear-gradient(90deg, var(--red-deep), var(--strip-red) 50%, var(--red-deep));
    text-align: center;
  }
  .product-name {
    margin: 10px 0 0;
    font-family: "Michroma", sans-serif;
    font-size: 25px;
    letter-spacing: 2px;
    color: var(--text-white);
  }
  .product-type {
    margin: 4px 0 0;
    font-family: "Michroma", sans-serif;
    font-size: 19px;
    color: var(--text-soft);
  }
  .stat-badges {
    position: absolute;
    left: 211px;
    top: 472px;
    display: flex;
    gap: 27px;
  }
  .stat-badge {
    width: 122px;
    height: 68px;
    background: linear-gradient(180deg, var(--silver-light) 0%, var(--silver-mid) 55%, var(--silver-dark) 100%);
    border: 1px solid #dcdcdc;
    text-align: center;
    color: var(--badge-ink);
    font-family: "Michroma", sans-serif;
  }
  .stat-value {
    display: block;
    margin-top: 6px;
    font-size: 26px;
    line-height: 1.1;
  }
  .stat-unit { font-size: 17px; }
  .stat-label {
    display: block;
    font-size: 12px;
    letter-spacing: 1px;
  }
</style>
</head>
<body>
  <main class="canvas">
    <section class="label">
      <div class="label-band">
        <h1 class="brand-name">VORGAN</h1>
        <p class="brand-descriptor">NUTRITION</p>
      </div>
      <div class="product-strip">
        <p class="product-name">LEAN MUSCLE BUILDER</p>
        <p class="product-type">Premium Whey Protein Blend</p>
      </div>
      <div class="stat-badges">
        <div class="stat-badge"><span class="stat-value">24<span class="stat-unit">G</span></span><span class="stat-label">PROTEIN</span></div>
        <div class="stat-badge"><span class="stat-value">9<span class="stat-unit">G</span></span><span class="stat-label">CARBS</span></div>
        <div class="stat-badge"><span class="stat-value">70</span><span class="stat-label">SERVINGS</span></div>
      </div>
    </section>
  </main>
</body>
</html>
```